A property investment company, looking to provide lovely sustainable homes for familys and individua

For a small investment business i am starting which will buy and refurbish unloved houses and apartments to rent out or resell. the company name is my family surname (HARGREAVE). <br/>i would like the design to be simple with maybe some emphasis on an ethical and sustainable/environmentally friendly approach with a branding of maybe trees blended with some houses and or apartments.<br/>The colours i like for this design would be mainly green on either a white or black background.
Target Market(s)
This business card is to be used for professional people such as estate agents
mortgage brokers, solicitors and trades people.
Industry/Entity Type
Real Estate
Contact Information for Business Card
owner/director-Martin hargreave
e-mail-martin@hwlettings.co.uk
website-hargreavehomeholdings.co.uk
mobile-07934560218
landline-02086543107

```html
<!DOCTYPE html>
<html lang="en">
<head>
<meta charset="utf-8">
<title>Hargreave Business Card</title>
<link rel="stylesheet" href="https://fonts.googleapis.com/css2?family=Open+Sans:wght@400;600;700&display=swap">
<style>
  :root {
    --backdrop: #e9e6e1;
    --card-white: #ffffff;
    --card-black: #0c0c0c;
    --leaf-green: #8cc63f;
    --leaf-green-light: #b5dc6e;
    --ink-dark: #3a3a3a;
    --ink-light: #ffffff;
    --rule-grey: #9a9a9a;
  }
  html, body {
    margin: 0;
    padding: 0;
    width: 1200px;
    height: 1022px;
    overflow: hidden;
    background: var(--backdrop);
    font-family: "Open Sans", Arial, sans-serif;
  }
  .business-card {
    position: absolute;
    left: 100px;
    top: 226px;
    width: 1000px;
    height: 570px;
    background: var(--card-white);
    box-shadow: 0 18px 40px rgba(0,0,0,0.25);
    overflow: hidden;
  }
  .card-shapes {
    position: absolute;
    inset: 0;
  }
  .brand-lockup {
    position: absolute;
    left: 110px;
    top: 254px;
    display: flex;
    align-items: center;
    gap: 16px;
  }
  .brand-dot {
    width: 34px;
    height: 34px;
    border-radius: 50%;
    background: var(--leaf-green);
  }
  .brand-name {
    font-weight: 700;
    font-size: 44px;
    letter-spacing: 2px;
    color: var(--ink-dark);
  }
  .holder {
    position: absolute;
    right: 42px;
    top: 18px;
    text-align: right;
  }
  .holder-name {
    font-weight: 700;
    font-size: 32px;
    color: var(--leaf-green);
    line-height: 1.15;
  }
  .holder-role {
    font-weight: 400;
    font-size: 20px;
    color: var(--ink-dark);
    line-height: 1.3;
  }
  .contact-list {
    position: absolute;
    right: 36px;
    top: 232px;
    list-style: none;
    margin: 0;
    padding: 0;
  }
  .contact-item {
    display: flex;
    justify-content: flex-end;
    align-items: center;
    gap: 14px;
    color: var(--ink-light);
    font-size: 21px;
    line-height: 36px;
  }
  .contact-icon {
    width: 20px;
    height: 20px;
    flex: none;
  }
</style>
</head>
<body>
  <div class="business-card">
    <svg class="card-shapes" width="1000" height="570" viewBox="0 0 1000 570">
      <g class="swoosh" transform="translate(0,12)">
        <path d="M1000,140 C800,140 600,200 510,340 C470,420 440,510 380,570 L1000,570 Z" fill="var(--card-black)"/>
        <path d="M1000,110 C790,112 580,182 488,330 C448,410 418,505 356,570 L374,570 C434,506 466,414 506,336 C596,194 800,128 1000,128 Z" fill="var(--leaf-green)"/>
        <path d="M1000,92 C780,96 560,170 468,320 C430,390 400,470 340,565 L346,568 C408,472 440,394 478,326 C570,178 790,100 1000,98 Z" fill="var(--leaf-green-light)"/>
        <path d="M430,440 C412,480 388,512 350,540 C392,518 418,486 434,442 Z" fill="var(--leaf-green)"/>
      </g>
      <line x1="110" y1="228" x2="440" y2="228" stroke="var(--rule-grey)" stroke-width="1.5"/>
      <line x1="110" y1="338" x2="440" y2="338" stroke="var(--rule-grey)" stroke-width="1.5"/>
    </svg>

    <div class="brand-lockup">
      <span class="brand-dot"></span>
      <span class="brand-name">HARGREAVE</span>
    </div>

    <div class="holder">
      <div class="holder-name">Martin hargreave</div>
      <div class="holder-role">Owner / Director</div>
    </div>

    <ul class="contact-list">
      <li class="contact-item">02 086 543 107
        <svg class="contact-icon" viewBox="0 0 24 24"><circle cx="12" cy="12" r="10" fill="none" stroke="var(--leaf-green)" stroke-width="2"/><path d="M8 7c0 5 4 9 9 9l1-2-3-1-1 1c-2-1-3-2-4-4l1-1-1-3z" fill="var(--leaf-green)"/></svg>
      </li>
      <li class="contact-item">07 934 560 218
        <svg class="contact-icon" viewBox="0 0 24 24"><rect x="6" y="2" width="12" height="20" rx="2" fill="none" stroke="var(--leaf-green)" stroke-width="2"/><rect x="10" y="17" width="4" height="2" fill="var(--leaf-green)"/></svg>
      </li>
      <li class="contact-item">martin@hwlettings.co.uk
        <svg class="contact-icon" viewBox="0 0 24 24"><rect x="2" y="5" width="20" height="14" fill="none" stroke="var(--leaf-green)" stroke-width="2"/><path d="M2 5l10 8 10-8" fill="none" stroke="var(--leaf-green)" stroke-width="2"/></svg>
      </li>
      <li class="contact-item">hargreavehomeholdings.co.uk
        <svg class="contact-icon" viewBox="0 0 24 24"><circle cx="12" cy="12" r="10" fill="var(--leaf-green)"/><path d="M2 12h20M12 2c-4 5-4 15 0 20M12 2c4 5 4 15 0 20" fill="none" stroke="var(--card-black)" stroke-width="1.5"/></svg>
      </li>
    </ul>
  </div>
</body>
</html>
```